Business Card Design

first side

having bramblewood kinder nest and all our contact details and then on the reverse side have
Megan Thorpe
Leadership & Service manager with the email placed underneath this.

Industry/Entity Type

Business

Contact Information for Business Card

Bramblewood Kinder Nest
214 Castlevane Rd, Larkfield 3187
Ph:9473 5581

www.bramblewoodkindernest.org.au

Megan Thorpe
Leadership & Service Manager
info@bkn.org.au

Requirements
Must have
• green similar to the logo color

this is a child care centre so we would like it funky looking and attractive

```html
<!DOCTYPE html>
<html lang="en">
<head>
<meta charset="utf-8">
<title>Bramblewood Kinder Nest – Business Card</title>
<link rel="stylesheet" href="https://fonts.googleapis.com/css2?family=Arimo:wght@400;700&display=swap">
<style>
  :root {
    --page-bg: #e4e5e7;
    --brand-green: #4fa33f;
    --brand-green-soft: #a9d07e;
    --card-white: #ffffff;
    --ink-grey: #4a4a4a;
    --card-shadow: rgba(0, 0, 0, 0.14);
  }
  * { box-sizing: border-box; margin: 0; padding: 0; }
  html, body {
    width: 1200px;
    height: 800px;
    overflow: hidden;
    background: var(--page-bg);
    font-family: "Arimo", Arial, sans-serif;
  }
  .stage {
    position: relative;
    width: 1200px;
    height: 800px;
    display: flex;
    align-items: center;
    justify-content: center;
    gap: 60px;
  }
  .card {
    position: relative;
    width: 525px;
    height: 300px;
    border-radius: 3px;
    box-shadow: 0 10px 28px var(--card-shadow);
    overflow: hidden;
  }

  /* Front side */
  .card--front {
    background: var(--brand-green);
    display: flex;
    align-items: center;
    justify-content: center;
  }
  .front-name {
    display: flex;
    align-items: center;
    gap: 14px;
  }
  .front-name__mark {
    width: 22px;
    height: 22px;
    border-radius: 50%;
    background: var(--brand-green-soft);
  }
  .front-name__text {
    color: var(--card-white);
    font-weight: 700;
    font-size: 30px;
    letter-spacing: 0.2px;
  }

  /* Reverse side */
  .card--back {
    background: var(--card-white);
    padding: 28px 34px;
  }
  .back-brand {
    display: flex;
    align-items: center;
    gap: 12px;
    margin-bottom: 18px;
  }
  .back-brand__mark {
    width: 16px;
    height: 16px;
    background: var(--brand-green);
  }
  .back-brand__text {
    color: var(--brand-green);
    font-weight: 700;
    font-size: 17px;
  }
  .address {
    font-style: normal;
    color: var(--ink-grey);
    font-size: 13px;
    line-height: 1.3;
    margin-bottom: 10px;
  }
  .contact-list {
    list-style: none;
    color: var(--ink-grey);
    font-size: 13px;
    line-height: 1.35;
  }
  .contact-list li {
    display: flex;
    align-items: center;
    gap: 8px;
  }
  .contact-icon {
    width: 12px;
    height: 12px;
    flex: none;
  }
  .person {
    position: absolute;
    right: 40px;
    bottom: 30px;
    text-align: right;
  }
  .person__name {
    color: var(--brand-green);
    font-weight: 700;
    font-size: 18px;
    margin-bottom: 4px;
  }
  .person__role {
    color: var(--ink-grey);
    font-size: 13px;
    line-height: 1.3;
  }
</style>
</head>
<body>
<main class="stage">

  <section class="card card--front" aria-label="Business card front">
    <div class="front-name">
      <span class="front-name__mark"></span>
      <span class="front-name__text">Bramblewood Kinder Nest</span>
    </div>
  </section>

  <section class="card card--back" aria-label="Business card reverse">
    <div class="back-brand">
      <span class="back-brand__mark"></span>
      <span class="back-brand__text">Bramblewood Kinder Nest</span>
    </div>

    <address class="address">
      Bramblewood Kinder Nest<br>
      214 Castlevane Rd<br>
      Larkfield 3187
    </address>

    <ul class="contact-list">
      <li>
        <svg class="contact-icon" viewBox="0 0 12 12" aria-hidden="true">
          <circle cx="6" cy="6" r="6" fill="var(--brand-green)"/>
          <path d="M3.8 3.2c.3-.3.7-.3.9 0l.6.8c.2.2.1.5-.1.7l-.3.3c.3.7.8 1.2 1.5 1.5l.3-.3c.2-.2.5-.3.7-.1l.8.6c.3.2.3.6 0 .9l-.4.4c-1.9.3-4.6-2.4-4.3-4.3z" fill="#fff"/>
        </svg>
        9473 5581
      </li>
      <li>
        <svg class="contact-icon" viewBox="0 0 12 12" aria-hidden="true">
          <circle cx="6" cy="6" r="6" fill="var(--brand-green)"/>
          <circle cx="6" cy="6" r="3.2" fill="none" stroke="#fff" stroke-width="0.9"/>
          <path d="M2.8 6h6.4M6 2.8c1.4 1.6 1.4 4.8 0 6.4M6 2.8c-1.4 1.6-1.4 4.8 0 6.4" fill="none" stroke="#fff" stroke-width="0.7"/>
        </svg>
        www.bramblewoodkindernest.org.au
      </li>
      <li>
        <svg class="contact-icon" viewBox="0 0 12 12" aria-hidden="true">
          <circle cx="6" cy="6" r="6" fill="var(--brand-green)"/>
          <rect x="3" y="3.8" width="6" height="4.4" fill="none" stroke="#fff" stroke-width="0.9"/>
          <path d="M3 3.8l3 2.5 3-2.5" fill="none" stroke="#fff" stroke-width="0.9"/>
        </svg>
        info@bkn.org.au
      </li>
    </ul>

    <div class="person">
      <p class="person__name">Megan Thorpe</p>
      <p class="person__role">Leadership<br>Service Manager</p>
    </div>
  </section>

</main>
</body>
</html>
```